Visitenkarten-Design für Psychiaterin
Zielgruppe
Dr. med. Monika Haberl, Ärztin, Psychotherapie für Kinder Jugendliche und Erwachsene, spezialisiert auf komplexe Posttraumatische Belastungsstörung, Dissoziative Störungen, Persönlichkeitsstörungen, Bindungsstörungen, LUMO-Mentorin
Das Design soll modern sein, Seriosität Professionalität, Dynamik und Geborgenheit ausstrahlen. Zielgruppe sind Menschen die traumatische Situationen überlebt haben.
Aufgabenstellung
Name, Fachgebiet und Spezialisierung, Telefonnummer, e-Mail
Unter Dateiupload sind Visitenkartenbeispiele die mir gefallen

```html
<!DOCTYPE html>
<html lang="de">
<head>
<meta charset="utf-8">
<title>Visitenkarte – Dr. med. Monika Haberl</title>
<link href="https://fonts.googleapis.com/css2?family=Questrial&family=Mulish:wght@700;800&display=swap" rel="stylesheet">
<style>
  :root {
    --page: #ffffff;
    --card: #ffffff;
    --ink: #3c3c3c;
    --orange: #ef9f5f;
    --peach: #f4ae72;
    --peach-light: #fad5a5;
    --plum: #a8487f;
    --shadow: rgba(0, 0, 0, 0.22);
  }
  * { box-sizing: border-box; margin: 0; padding: 0; }
  html, body {
    width: 868px;
    height: 1200px;
    overflow: hidden;
    background: var(--page);
  }
  body {
    position: relative;
    font-family: "Questrial", "Century Gothic", sans-serif;
    color: var(--ink);
  }
  .card {
    position: absolute;
    left: 14px;
    width: 806px;
    height: 521px;
    background: var(--card);
    border-radius: 38px;
    box-shadow: 10px 12px 18px var(--shadow);
    overflow: hidden;
  }
  .card--front { top: 18px; }
  .card--back { top: 635px; }

  /* Front */
  .audience,
  .website-vertical {
    position: absolute;
    writing-mode: vertical-rl;
    transform: rotate(180deg);
    letter-spacing: 0.3px;
    white-space: nowrap;
  }
  .audience {
    left: 44px;
    bottom: 52px;
    font-size: 26px;
    color: var(--orange);
  }
  .website-vertical {
    right: 32px;
    bottom: 52px;
    font-size: 27px;
    color: var(--plum);
  }
  .mark-area {
    position: absolute;
    left: 276px;
    top: 52px;
    width: 282px;
    height: 236px;
    border-radius: 48% 52% 20% 30% / 55% 60% 10% 20%;
    background: linear-gradient(120deg, rgba(168,72,127,0.55) 0%, var(--peach) 45%, var(--peach-light) 100%);
  }
  .title-block {
    position: absolute;
    left: 229px;
    top: 322px;
  }
  .title-block .degree {
    font-size: 51px;
    line-height: 52px;
    letter-spacing: -0.5px;
  }
  .title-block .name {
    font-family: "Mulish", "Century Gothic", sans-serif;
    font-weight: 800;
    font-size: 50px;
    line-height: 54px;
    letter-spacing: -0.8px;
  }
  .title-block .field {
    margin-top: 12px;
    font-size: 25px;
    letter-spacing: 5.6px;
  }

  /* Back */
  .network-area {
    position: absolute;
    left: 57px;
    top: 40px;
    width: 376px;
    height: 342px;
    border-radius: 45% 55% 40% 50% / 50% 45% 55% 50%;
    background:
      radial-gradient(circle at 70% 30%, var(--peach-light) 0%, rgba(250,213,165,0.6) 40%, transparent 70%),
      radial-gradient(circle at 30% 75%, rgba(168,72,127,0.75) 0%, rgba(168,72,127,0.3) 45%, transparent 72%),
      radial-gradient(circle at 45% 50%, rgba(244,174,114,0.5) 0%, transparent 60%);
  }
  .contact {
    position: absolute;
    right: 64px;
    top: 136px;
    text-align: right;
    font-size: 27px;
    line-height: 32px;
  }
  .contact .degree { font-size: 30px; line-height: 30px; }
  .contact .name {
    font-family: "Mulish", "Century Gothic", sans-serif;
    font-weight: 800;
    font-size: 32px;
    line-height: 36px;
    letter-spacing: -0.4px;
  }
  .contact .address { margin-top: 36px; }
  .contact .reach { margin-top: 34px; }
</style>
</head>
<body>

  <section class="card card--front">
    <p class="audience">Kinder | Jugendliche | Erwachsene</p>
    <div class="mark-area" role="img" aria-label="Praxiszeichen: zwei Kopfprofile mit Netzwerk aus Kreisen in Pflaume und Pfirsich"></div>
    <div class="title-block">
      <p class="degree">Dr. med.</p>
      <p class="name">Monika Haberl</p>
      <p class="field">PSYCHOTHERAPIE</p>
    </div>
    <p class="website-vertical">www.psychotherapie-haberl.de</p>
  </section>

  <section class="card card--back">
    <div class="network-area" role="img" aria-label="Große dekorative Fläche: verbundene Kreise in Pflaume, Orange und Pfirsich"></div>
    <div class="contact">
      <p class="degree">Dr. med.</p>
      <p class="name">Monika Haberl</p>
      <p class="address">Lindenweg 24<br>54321 Auenstadt</p>
      <p class="reach">Fon 07531 482960<br>Fax 07531 482961<br>haberl@praxis-haberl.de<br>www.psychotherapie-haberl.de</p>
    </div>
  </section>

</body>
</html>
```